Regional Consulting Business Needs a Business Card Design

We need a business card design for our new business based in Regional Victoria, Australia called Brindle Power. We are a consulting company with our main goal being to save people momey money and reducing their carbon footprint. Anything from water saving showerheads, to energy saving lightglobes and even to solar power. We would like to see designs that use bright colours. The final design should shout 'we are here to help you'.

Industry/Entity Type

Business

```html
<!DOCTYPE html>
<html lang="en">
<head>
<meta charset="UTF-8">
<title>Brindle Power — Business Card</title>
<link href="https://fonts.googleapis.com/css2?family=Open+Sans:wght@400;600;700;800&display=swap" rel="stylesheet">
<style>
  :root {
    --backdrop: #f3f4f4;
    --frame: #e6e8e8;
    --card-blue: #0044dd;
    --card-blue-deco: #0b5cf6;
    --card-yellow: #ffe600;
    --card-yellow-deco: #fff31c;
    --ink-white: #ffffff;
    --ink-blue: #1a3fbf;
  }
  * { margin: 0; padding: 0; box-sizing: border-box; }
  html, body {
    width: 1200px;
    height: 900px;
    overflow: hidden;
    background: var(--backdrop);
    font-family: "Open Sans", sans-serif;
  }
  .stage {
    position: relative;
    width: 1200px;
    height: 900px;
    border: 12px solid var(--frame);
    background: var(--backdrop);
  }
  .card {
    position: absolute;
    width: 519px;
    height: 295px;
    overflow: hidden;
  }
  .card-front {
    left: 295px;
    top: 173px;
    background: var(--card-blue);
  }
  .card-back {
    left: 609px;
    top: 531px;
    background: var(--card-yellow);
  }
  .card-deco {
    position: absolute;
    left: -6px;
    bottom: -30px;
    font-weight: 800;
    font-size: 142px;
    line-height: 1;
    letter-spacing: 2px;
    white-space: nowrap;
  }
  .card-front .card-deco { color: var(--card-blue-deco); }
  .card-back .card-deco { color: var(--card-yellow-deco); }
  .brand {
    position: absolute;
    left: 0;
    right: 0;
    top: 98px;
    text-align: center;
    color: var(--ink-white);
  }
  .brand-name {
    font-weight: 400;
    font-size: 35px;
    line-height: 1;
    letter-spacing: 0.5px;
  }
  .brand-tagline {
    margin-top: 6px;
    font-size: 16.5px;
  }
  .slogan {
    position: absolute;
    left: 0;
    right: 0;
    top: 222px;
    text-align: center;
    color: var(--ink-white);
    font-size: 26px;
    line-height: 1;
  }
  .person {
    position: absolute;
    left: 188px;
    top: 107px;
    color: var(--ink-blue);
    font-size: 18.5px;
    line-height: 25px;
  }
  .person-name { font-weight: 700; }
  .contact {
    position: absolute;
    left: 190px;
    top: 212px;
    color: var(--ink-blue);
    font-size: 16.5px;
    line-height: 21px;
  }
</style>
</head>
<body>
  <main class="stage">
    <section class="card card-front">
      <div class="card-deco" aria-hidden="true">POWER</div>
      <div class="brand">
        <div class="brand-name">BRINDLE POWER</div>
        <div class="brand-tagline">Maintanence &amp; Consulting Services</div>
      </div>
      <p class="slogan">“WE ARE HERE TO HELP YOU!”</p>
    </section>

    <section class="card card-back">
      <div class="card-deco" aria-hidden="true">POWER</div>
      <div class="person">
        <div class="person-name">Alan Reeve</div>
        <div class="person-role">CEO</div>
      </div>
      <address class="contact" style="font-style: normal;">
        <div>1234 xxxx xxxxx Rd Australia xxxx</div>
        <div>000.0000.0000</div>
        <div>alanreeve@xxxx.com</div>
      </address>
    </section>
  </main>
</body>
</html>
```